Rack card 4"x9" for a construction company

We need to have a design for:
- the holder of rack cards. Letter size
- and the rack cards. Size 4"x9"

I attached a picture of the sample holder for example.

I am putting some of the brochures and pics we have in:

https://files.vendoshare.net/folders/7QpT3wXz9KmB2rLvN8cYd4HsJ6fGaE5uVo?usp=sharing

The Bodoni font is on the drive.
The rack card should call to action - to learn about our projects and that we are offering fixed price packages.

One of the sides of the rack card has to show our houses like we show on the website birchwell-builders.ca
Images with short info like on the website http://www.birchwell-builders.ca/our-projects/
Maybe have something like: Learn more about our recent projects at www...

You can use our logo from th pdf files. In the brochure on the cover page we show all the associations we are member of - this is a must to be shown.

Mentioning the website and the phone number is a must.

Bring your ideas.
Don't hesitate to ask questions.

Thanks
Dorian

```html
<!DOCTYPE html>
<html lang="en">
<head>
<meta charset="utf-8">
<title>Birchwell Builders – Rack Card Panels</title>
<link href="https://fonts.googleapis.com/css2?family=Bodoni+Moda:wght@500;700&family=Zilla+Slab:wght@500;600&family=Josefin+Sans:wght@400;600;700&family=Oswald:wght@500&display=swap" rel="stylesheet">
<style>
  :root{
    --navy:#1c2b55;
    --navy-deep:#0f1c3e;
    --blue:#25467f;
    --khaki:#8b876f;
    --khaki-light:#a5a189;
    --ink:#1f2437;
    --white:#ffffff;
    --paper:#eeeeec;
    --bg:#f2efe9;
  }
  *{box-sizing:border-box;margin:0;padding:0}
  html,body{width:1200px;height:1200px;overflow:hidden;background:var(--bg)}
  body{position:relative;font-family:"Josefin Sans",sans-serif}

  .card{position:absolute;left:60px;width:1080px;height:480px;overflow:hidden;box-shadow:0 4px 14px rgba(0,0,0,.25)}
  .card--projects{top:86px;background:linear-gradient(135deg,#2d4f8c 0%,var(--navy) 55%,var(--navy-deep) 100%)}
  .card--dream{top:632px;background:var(--navy-deep)}

  /* brand block */
  .brand{position:absolute;display:flex;flex-direction:column;align-items:center;justify-content:center;text-align:center;color:var(--ink);font-family:"Bodoni Moda",serif;font-weight:700;white-space:nowrap}
  .brand__name{font-size:31px;letter-spacing:1px;line-height:1}
  .brand__sub{font-size:14px;letter-spacing:4px;margin-top:10px}

  .side-logo{position:absolute;left:0;top:0;width:275px;height:226px;background:var(--white)}
  .side-logo .brand{inset:0}
  .about{position:absolute;left:0;top:226px;width:275px;height:254px;background:var(--khaki);color:var(--white);padding:18px 30px 0 28px}
  .about__title{font-size:25px;font-weight:400;display:inline-block;border-bottom:1.5px solid var(--white);padding-bottom:2px;margin-bottom:14px}
  .about__text{font-size:15px;line-height:18.5px;text-align:justify}

  .headline{position:absolute;left:275px;right:0;color:var(--white);font-family:"Bodoni Moda",serif;font-weight:700;text-align:center;line-height:1.08}
  .card--projects .headline{top:20px;font-size:40px}
  .lede{position:absolute;color:var(--white);text-align:center;font-size:16px;line-height:20px}
  .card--projects .lede{left:300px;right:20px;top:126px}

  .projects{position:absolute;left:294px;top:183px;display:flex;gap:22px}
  .project{width:176px;height:242px;background:var(--white);border:3px solid var(--white);display:flex;flex-direction:column}
  .project__photo{height:144px}
  .project__title{flex:1;font-family:"Zilla Slab",serif;font-weight:600;color:var(--ink);font-size:16.5px;line-height:17px;padding:7px 8px 0}
  .project__stats{height:50px;background:var(--khaki);display:flex;align-items:center;justify-content:space-around;color:var(--white);text-align:center}
  .stat{padding:0 4px}
  .stat + .stat{border-left:1px solid var(--white)}
  .stat__label{font-size:10px;display:block}
  .stat__value{font-size:14px;display:block;margin-top:3px}

  .contact-bar{position:absolute;right:0;bottom:0;height:40px;width:530px;background:var(--khaki);clip-path:polygon(34px 0,100% 0,100% 100%,0 100%);display:flex;align-items:center;justify-content:flex-end;gap:10px;padding-right:18px;color:var(--white)}
  .contact-bar__web{font-size:20px;display:flex;align-items:center;gap:10px}
  .contact-bar__web b{font-weight:700}
  .contact-bar__divider{width:2px;height:28px;background:var(--white);margin:0 4px}
  .contact-bar__phone{font-family:"Oswald",sans-serif;font-weight:500;font-size:24px;display:flex;align-items:center;gap:8px}

  /* dream card */
  .hero-photo{position:absolute;inset:0 0 66px 0;background:linear-gradient(100deg,#b59c86 0%,#8c7d73 22%,#5f6271 40%,#33405f 62%,#1a2748 100%)}
  .hero-shade{position:absolute;inset:0 0 66px 0;background:linear-gradient(90deg,rgba(15,28,62,0) 25%,rgba(15,28,62,.55) 60%,rgba(15,28,62,.75) 100%)}
  .ribbon{position:absolute;left:35px;top:0;width:238px;height:238px;background:var(--white);clip-path:polygon(0 0,100% 0,100% 100%,50% 77%,0 100%)}
  .ribbon-edge{position:absolute;left:35px;top:0;width:238px;height:246px;background:var(--navy);clip-path:polygon(0 0,100% 0,100% 100%,50% 79%,0 100%)}
  .ribbon .brand{left:0;right:0;top:0;height:190px}
  .ribbon .brand__name{font-size:28px}
  .ribbon .brand__sub{font-size:13px}
  .card--dream .headline{left:380px;right:20px;top:30px;font-size:48px}
  .card--dream .lede{left:395px;right:40px;top:150px}
  .gallery{position:absolute;left:513px;top:226px;display:flex;gap:32px}
  .gallery__photo{width:191px;height:157px;border:3px solid var(--white)}

  .members{position:absolute;left:0;right:0;bottom:0;height:66px;background:var(--paper);display:flex;align-items:center;padding-left:33px}
  .members__label{font-family:"Bodoni Moda",serif;font-weight:700;font-size:22px;color:var(--ink);letter-spacing:.5px;margin-right:26px;white-space:nowrap}
  .badges{display:flex;align-items:center;gap:26px}
  .badge{background:#c9ccd3}
  .members__divider{width:2px;height:40px;background:var(--ink);margin:0 14px 0 22px}
  .members__web{font-size:19px;color:var(--ink);display:flex;align-items:center;gap:10px}
  .members__web b{font-weight:700}
</style>
</head>
<body>

<section class="card card--projects">
  <div class="side-logo">
    <div class="brand"><span class="brand__name">BIRCHWELL</span><span class="brand__sub">BUILDERS LTD</span></div>
  </div>
  <div class="about">
    <h2 class="about__title">About us</h2>
    <p class="about__text">Birchwell Builders Ltd Founder, Dorian Kessler, is a third-generation home builder. Growing up, he was exposed daily to incredible examples of fine construction and craftsmanship. These early lessons ignited a passion for creating masterful single family homes for others</p>
  </div>

  <h1 class="headline">Exquisite, Cost-effective Custom Builds:<br>Your Vision. Your Reality</h1>
  <p class="lede">Here is some of our finest work. Each is an example of a vision we turned to reality using only the highest quality building materials.Tremendous craftsmanship takes work. We're happy to oblige.</p>

  <div class="projects">
    <article class="project">
      <div class="project__photo" role="img" aria-label="Photo of a dark grey traditional craftsman house under a cloudy sky" style="background:linear-gradient(180deg,#b8cde0 0%,#6b7178 45%,#3d4244 75%,#5c7a3a 100%)"></div>
      <h3 class="project__title">Renfrew Traditional Craftsman</h3>
      <div class="project__stats">
        <div class="stat"><span class="stat__label">BEDROOMS</span><span class="stat__value">7</span></div>
        <div class="stat"><span class="stat__label">BATH</span><span class="stat__value">5</span></div>
        <div class="stat"><span class="stat__label">SQFT</span><span class="stat__value">3828</span></div>
      </div>
    </article>
    <article class="project">
      <div class="project__photo" role="img" aria-label="Photo of a large stone and timber modern craftsman house with landscaped lawn" style="background:linear-gradient(180deg,#5d7fb0 0%,#4c4f52 40%,#6e6a5f 70%,#5f8a3c 100%)"></div>
      <h3 class="project__title">Burnaby Modern Craftsman</h3>
      <div class="project__stats">
        <div class="stat"><span class="stat__label">BEDROOMS</span><span class="stat__value">8</span></div>
        <div class="stat"><span class="stat__label">BATH</span><span class="stat__value">8</span></div>
        <div class="stat"><span class="stat__label">SQFT</span><span class="stat__value">7973</span></div>
      </div>
    </article>
    <article class="project">
      <div class="project__photo" role="img" aria-label="Photo of a lit white modern craftsman house at dusk" style="background:linear-gradient(180deg,#1d3f8f 0%,#3b5aa0 35%,#b9b6ad 65%,#4b4b4b 100%)"></div>
      <h3 class="project__title">Renfrew Modern Craftsman</h3>
      <div class="project__stats">
        <div class="stat"><span class="stat__label">BEDROOMS</span><span class="stat__value">9</span></div>
        <div class="stat"><span class="stat__label">BATH</span><span class="stat__value">7</span></div>
        <div class="stat"><span class="stat__label">SQFT</span><span class="stat__value">4020</span></div>
      </div>
    </article>
    <article class="project">
      <div class="project__photo" role="img" aria-label="Photo of a white modern house with stone steps and green lawn" style="background:linear-gradient(180deg,#2a57b5 0%,#d9d6cf 45%,#a9a59c 75%,#5c9a3a 100%)"></div>
      <h3 class="project__title">Kerrisdale Modern Opulence</h3>
      <div class="project__stats">
        <div class="stat"><span class="stat__label">BEDROOMS</span><span class="stat__value">7</span></div>
        <div class="stat"><span class="stat__label">BATH</span><span class="stat__value">5</span></div>
        <div class="stat"><span class="stat__label">SQFT</span><span class="stat__value">3828</span></div>
      </div>
    </article>
  </div>

  <div class="contact-bar">
    <span class="contact-bar__web">
      <svg width="28" height="28" viewBox="0 0 28 28" fill="none" stroke="#fff" stroke-width="1.6"><circle cx="14" cy="14" r="12.5"/><circle cx="14" cy="14" r="8.5"/><ellipse cx="14" cy="14" rx="3.5" ry="8.5"/><path d="M5.5 14h17M7 10h14M7 18h14"/></svg>
      <span>www.<b>birchwell-builders</b>.ca</span>
    </span>
    <span class="contact-bar__divider"></span>
    <span class="contact-bar__phone">
      <svg width="28" height="28" viewBox="0 0 28 28" fill="none" stroke="#fff" stroke-width="1.8"><circle cx="14" cy="14" r="12.5"/><path d="M10 8.5l2 3-1.4 1.6c.8 1.8 2 3 3.8 3.8l1.6-1.4 3 2-1.2 2c-4.5 0-9.7-5.2-9.7-9.7z" fill="#fff" stroke="none"/></svg>
      604.555.0182
    </span>
  </div>
</section>

<section class="card card--dream">
  <div class="hero-photo" role="img" aria-label="Photo of a modern white luxury house facade at dusk beside a neighbouring home"></div>
  <div class="hero-shade"></div>
  <div class="ribbon-edge"></div>
  <div class="ribbon">
    <div class="brand"><span class="brand__name">BIRCHWELL</span><span class="brand__sub">BUILDERS LTD</span></div>
  </div>

  <h1 class="headline">Build The Home Of<br>Your Dreams in Vancouver</h1>
  <p class="lede">Birchwell Builders has a dedicated, experienced staff of professionals standing at the ready to make the vision you have for your dream home a reality. Click the Play Button on the video above to learn more.</p>

  <div class="gallery">
    <div class="gallery__photo" role="img" aria-label="Photo of a white modern house with front stairs and lawn" style="background:linear-gradient(180deg,#8fb2d6 0%,#e0dbd0 45%,#8e8a80 75%,#4f8a2e 100%)"></div>
    <div class="gallery__photo" role="img" aria-label="Photo of a blue craftsman house behind a black iron fence" style="background:linear-gradient(180deg,#5a8fd0 0%,#6f86a8 45%,#3f4c66 75%,#3f7a2c 100%)"></div>
  </div>

  <footer class="members">
    <span class="members__label">PROUD MEMBERS OF</span>
    <div class="badges">
      <span class="badge" style="width:58px;height:40px;border-radius:50%"></span>
      <span class="badge" style="width:64px;height:40px"></span>
      <span class="badge" style="width:40px;height:40px"></span>
      <span class="badge" style="width:56px;height:40px"></span>
      <span class="badge" style="width:88px;height:30px;border-radius:3px"></span>
    </div>
    <span class="members__divider"></span>
    <span class="members__web">
      <svg width="26" height="26" viewBox="0 0 28 28" fill="none" stroke="#1f2437" stroke-width="1.6"><circle cx="14" cy="14" r="12.5"/><circle cx="14" cy="14" r="8.5"/><ellipse cx="14" cy="14" rx="3.5" ry="8.5"/><path d="M5.5 14h17M7 10h14M7 18h14"/></svg>
      <span>www.<b>birchwell-builders</b>.ca</span>
    </span>
  </footer>
</section>

</body>
</html>
```